Leap! Maximizing the Transfer of a Company to Seasoned Buyers

We are a private equity firm, and the partners wrote this book to help business owners understand the process for selling their business. We need a cover for the book, and our current thinking is a picture of a person (or just the leg/foot w/business shoe) walking out a door, representing our title "Leap!"
Business owners will benefit from learning what professional investors, like private equity firms, are looking for and how the process is likely to unfold. Business owners will also learn how to prepare their company and themselves for this process.

Target Market(s)

Small to medium sized business owners

Font styles to use
Serif

Colors
3277b5
3276b5
85acd3
cfdeed

Requirements
Must have
• a professional look and feel that will attract business owners and a compelling call to action for those business owners considering a sale of their business
Nice to have
• Leverage the same color blue and possibly logo from Birch Hollow Capital, which can be seen here - https://birchhollowcap.example/
Should not have
• humor/quirkiness/schtick

```html
<!DOCTYPE html>
<html lang="en">
<head>
<meta charset="utf-8">
<title>Leap! Maximizing the Transfer of a Company to Seasoned Buyers</title>
<link rel="stylesheet" href="https://fonts.googleapis.com/css2?family=Saira+Extra+Condensed:wght@400;600&display=swap">
<style>
  :root {
    --navy-deep: #001a40;
    --navy: #022a5c;
    --blue-glow: #3277b5;
    --blue-light: #85acd3;
    --title-fill: #cfdeed;
    --title-shadow: #000814;
    --subtitle: #dce8f4;
  }
  html, body {
    margin: 0;
    padding: 0;
    width: 840px;
    height: 1200px;
    overflow: hidden;
    background: var(--navy-deep);
  }
  .cover {
    position: relative;
    width: 840px;
    height: 1200px;
    overflow: hidden;
    background: radial-gradient(ellipse 60% 50% at 50% 42%, #0a3a72 0%, var(--navy) 50%, var(--navy-deep) 100%);
  }
  .doorway-scene {
    position: absolute;
    left: 0;
    top: 0;
    width: 840px;
    height: 760px;
  }
  .cover-type {
    position: absolute;
    left: 0;
    top: 0;
    width: 840px;
    height: 1200px;
  }
  .title {
    font-family: "Saira Extra Condensed", "Arial Narrow", sans-serif;
    font-weight: 600;
    font-size: 272px;
    fill: var(--title-fill);
  }
  .title-shadow {
    fill: var(--title-shadow);
  }
  .subtitle {
    font-family: "Saira Extra Condensed", "Arial Narrow", sans-serif;
    font-weight: 400;
    font-size: 40px;
    fill: var(--subtitle);
  }
</style>
</head>
<body>
  <main class="cover">
    <svg class="doorway-scene" viewBox="0 0 840 760" role="img" aria-label="Photograph: silhouette of a businessman with a briefcase walking through a bright doorway toward a night city skyline, casting a shadow on the floor">
      <defs>
        <linearGradient id="doorLight" x1="0" y1="0" x2="0" y2="1">
          <stop offset="0" stop-color="#2a5d9a"/>
          <stop offset="0.45" stop-color="#6f9ad6"/>
          <stop offset="0.8" stop-color="#3277b5"/>
          <stop offset="1" stop-color="#1c6aa8"/>
        </linearGradient>
        <radialGradient id="floorGlow" cx="0.5" cy="0.35" r="0.6">
          <stop offset="0" stop-color="#4ab0e0" stop-opacity="0.8"/>
          <stop offset="1" stop-color="#022a5c" stop-opacity="0"/>
        </radialGradient>
        <filter id="soft"><feGaussianBlur stdDeviation="20"/></filter>
      </defs>
      <rect x="166" y="-20" width="492" height="660" fill="url(#doorLight)" filter="url(#soft)" opacity="0.85"/>
      <rect x="176" y="0" width="472" height="628" fill="url(#doorLight)"/>
      <ellipse cx="420" cy="675" rx="330" ry="75" fill="url(#floorGlow)"/>
    </svg>
    <svg class="cover-type" viewBox="0 0 840 1200">
      <text class="title title-shadow" x="423" y="945" text-anchor="middle" textLength="500" lengthAdjust="spacingAndGlyphs">LEAP!</text>
      <text class="title" x="420" y="942" text-anchor="middle" textLength="500" lengthAdjust="spacingAndGlyphs">LEAP!</text>
      <text class="subtitle" x="420" y="1028" text-anchor="middle" textLength="660" lengthAdjust="spacingAndGlyphs">Maximizing the Transfer of a Company to Seasoned Buyers</text>
    </svg>
  </main>
</body>
</html>
```